unique professional wordpress website design for high end limo rental / car rental company

We need a elegant and professional website (ready to use wordpress theme) for a Car rental / Transport services company. We provide luxury cars on rental and lease. Website needs to be unique, high end and classy and should project the brand name and value proposition. It should not be similar to any existing websites with the same or similar brand name and category. Files should be as a ready to use wordpress 4.7 compatible theme file and should include images and video (stock footage) or links to the stock items used.

Home page should have a full width video background similar to the link below. Something similar can be used.

https://www.videohost-example.com/watch?v=Qz3rT_wmx8P

Menu Structure:
Home (Video background, menu)

Vehicles (banner, two column design with alternate image and content)

Services ( Events, Shuttle Services, Airport Limo, Executive Limo, Point to Point) Seperate page for each sub menu with 2 column content and image

Prices (Drop down selection for start point and end point) also can be selected from map.

Gallery (Video and image gallery - Thumbnail view)

About us : Content and images in alternating blocks

Contact Us : Address, contact details, location map, and Contact us form (Name, email address, Mobile phone, Query / Question) and send button. to be connected to email address later.

Website Footer to have the following (Testimonials single line text moving), Social media icons along with likes / tweets number only, and hyperlink. Contact address, and Newsletter subscription.

Book now Button will lead to the Booking page and payment gateway. Will be done seperately

Header will have Contact numbers, Access email (Button) Book now (Button)

Company : Orvane Limousine
domain : https://www.orvane-example.limo
Sector : Transport solutions, taxi, vehicle rental, chauffer services
Preferred colors : Blue, White, Gold, Black

Files should be compatible with Wordpress 4.7, and should optionally have html/css included along with stock images and video / links.

Target Market(s)

B2B, Transport

Industry/Entity Type

Travel Industry

Font styles to use
Serif
Sans Serif

Requirements
Must have
• Wordpress theme files, HTML/CSS, images and video (links)
Nice to have
• ecommerce page design for cab booking, similar to this:
• https://book.tarvixcoaches-example.com/BookingApp/FastBooking?y
Should not have
• no copy paste or using existing commercial wordpress templates.

```html
<!DOCTYPE html>
<html lang="en">
<head>
<meta charset="utf-8">
<title>Orvane Limousine</title>
<link href="https://fonts.googleapis.com/css2?family=Open+Sans:ital,wght@0,300;0,400;0,600;0,700;1,400&display=swap" rel="stylesheet">
<style>
:root{
  --gold:#c9a04a;
  --ink:#2b2b2b;
  --light:#efefef;
  --white:#fff;
  --footer:#262626;
  --footer-base:#1c1c1c;
  --footer-text:#9a9a9a;
  --tweet:#1da1f2;
}
*{box-sizing:border-box;margin:0;padding:0}
html,body{width:1200px;height:2174px;overflow:hidden}
body{font-family:"Open Sans",Arial,sans-serif;color:var(--ink);background:var(--white);position:relative}
a{color:inherit;text-decoration:none}

/* hero */
.hero{position:absolute;left:0;top:0;width:1200px;height:641px;overflow:hidden;
  background:linear-gradient(180deg,#1d1b1d 0%,#3e302c 22%,#8a5a3a 40%,#a8703f 47%,#5e4536 58%,#33302f 75%,#2e2d2d 100%)}
.logo{position:absolute;left:43px;top:30px;width:125px;text-align:center}
.logo-mark{width:30px;height:30px;border-radius:50%;background:var(--gold);margin:0 auto 12px}
.logo-name{font-size:26px;font-weight:400;letter-spacing:2px;color:var(--gold)}
.call{position:absolute;left:757px;top:35px;font-size:11.5px;color:var(--white);display:flex;align-items:center;gap:6px}
.call b{font-weight:400;color:var(--gold)}
.pill{position:absolute;height:30px;border-radius:15px;background:var(--gold);color:var(--white);
  font-size:10.5px;display:flex;align-items:center;justify-content:center;text-transform:uppercase}
.nav{position:absolute;top:86px;left:0;font-size:11.5px;color:var(--white);text-transform:uppercase}
.nav span{position:absolute;white-space:nowrap}
.nav i{font-style:normal;font-size:9px;margin-left:6px}
.play{position:absolute;left:557px;top:277px}
.hero-sub{position:absolute;left:690px;top:246px;font-size:23px;font-weight:300;color:var(--white);text-transform:uppercase}
.hero-title{position:absolute;left:690px;top:280px;font-size:45px;font-weight:700;color:var(--white);text-transform:uppercase;letter-spacing:.5px}
.btn-outline-light{position:absolute;left:694px;top:361px;width:186px;height:45px;border:2px solid var(--white);border-radius:23px;
  color:var(--white);font-size:15px;font-weight:600;display:flex;align-items:center;justify-content:center}

/* services */
.services{position:absolute;left:0;top:641px;width:1200px;height:385px;background:var(--light)}
.section-title{font-size:29px;font-weight:700;text-transform:uppercase;color:var(--ink)}
.services .section-title{position:absolute;top:60px;width:1200px;text-align:center}
.services .lead{position:absolute;top:111px;width:1200px;text-align:center;font-size:15px;color:#444}
.service{position:absolute;top:182px;width:170px;text-align:center}
.service svg{display:block;margin:0 auto}
.service h3{font-size:14px;font-weight:700;margin-top:10px;text-transform:uppercase}

/* vehicles */
.vehicles-title{position:absolute;left:99px;top:1087px}
.vehicles-lead{position:absolute;left:99px;top:1138px;font-size:14px;color:#333}
.btn-outline{position:absolute;border:1.5px solid var(--gold);border-radius:23px;color:var(--gold);
  font-size:12.5px;font-weight:600;display:flex;align-items:center;justify-content:center;text-transform:uppercase}
.vehicle-photo{position:absolute;top:1207px;width:287px;height:197px}
.vehicle-info{position:absolute;top:1212px;width:200px}
.vehicle-info h4{font-size:14px;font-weight:700;text-transform:uppercase;margin-bottom:10px}
.vehicle-info li{list-style:none;font-size:12.5px;line-height:26px;color:#333}
.vehicle-info li::before{content:"›";color:#c0392b;font-weight:700;margin-right:10px}
.price{font-size:12.5px;margin-top:4px}
.price b{font-size:26px;font-weight:400;color:var(--gold);margin-left:3px}
.btn-gold{display:flex;width:100px;height:26px;border-radius:13px;background:var(--gold);color:var(--white);
  font-size:10px;align-items:center;justify-content:center;text-transform:uppercase;margin-top:8px}
.arrow{position:absolute;top:1284px}

/* about */
.about-photo{position:absolute;left:87px;top:1507px;width:623px;height:203px;
  background:linear-gradient(90deg,#f4f5f8 0%,#e7e9ef 50%,#f6f3f3 100%)}
.about-title{position:absolute;left:753px;top:1495px}
.about-text{position:absolute;left:753px;top:1544px;width:375px;font-size:13px;line-height:25.5px;color:#555}

/* footer */
.footer{position:absolute;left:0;top:1776px;width:1200px;height:398px;background:var(--footer);color:var(--footer-text)}
.testimonial{position:absolute;left:0;top:0;width:1200px;height:76px;border-bottom:1px solid #333;display:flex;align-items:center;padding-left:99px;font-size:12.5px;font-style:italic}
.avatar{width:42px;height:42px;border-radius:50%;background:#8f7c6a;margin-right:14px;flex:none}
.testimonial b{font-weight:400;color:var(--gold);margin-right:4px}
.fcol{position:absolute;top:111px}
.fcol h5{font-size:13px;font-weight:700;color:var(--gold);text-transform:uppercase;margin-bottom:14px}
.fcol li{list-style:none;font-size:11.5px;line-height:27.5px}
.fcol p{font-size:11.5px;line-height:22px}
.email-field{width:301px;height:33px;border:1px solid #444;border-radius:17px;margin-top:14px;padding-left:22px;font-size:11.5px;display:flex;align-items:center;color:#bbb}
.fbtn{width:113px;height:33px;border:1.5px solid var(--gold);border-radius:17px;color:var(--white);font-size:10.5px;display:flex;align-items:center;justify-content:center;margin-top:13px;text-transform:uppercase}
.contact-line{display:flex;align-items:center;gap:9px;font-size:11.5px;margin-top:8px}
.tweet{width:83px;height:29px;border-radius:15px;background:var(--tweet);color:var(--white);font-size:12px;display:flex;align-items:center;justify-content:center;gap:6px;margin-top:26px}
.tweet span{width:9px;height:9px;border-radius:50%;background:var(--white)}
.footer-base{position:absolute;left:0;top:334px;width:1200px;height:64px;background:var(--footer-base);font-size:11px}
.footer-base .copy{position:absolute;left:103px;top:25px}
.footer-base .social{position:absolute;left:776px;top:25px;display:flex;align-items:center;gap:16px}
.dot{width:10px;height:10px;border-radius:50%;border:1px solid #888;display:inline-block}
</style>
</head>
<body>

<header class="hero" role="img" aria-label="Background video: luxury car driving along a highway at sunset">
  <div class="logo"><div class="logo-mark"></div><div class="logo-name">ORVANE</div></div>

  <div class="call">
    <svg width="12" height="12" viewBox="0 0 24 24"><path fill="#c9a04a" d="M6.6 10.8a15 15 0 0 0 6.6 6.6l2.2-2.2c.3-.3.7-.4 1-.2 1.1.4 2.3.6 3.6.6.6 0 1 .4 1 1V20c0 .6-.4 1-1 1A17 17 0 0 1 3 4c0-.6.4-1 1-1h3.5c.6 0 1 .4 1 1 0 1.3.2 2.5.6 3.6.1.3 0 .7-.2 1z"/></svg>
    Call Us : <b>( 555 ) 014 2290</b>
  </div>
  <a class="pill" style="left:930px;top:28px;width:99px">Subscribe</a>
  <a class="pill" style="left:1043px;top:28px;width:99px">Book Now</a>

  <nav class="nav">
    <span style="left:494px">Home</span>
    <span style="left:578px">Vehicles<i>⌄</i></span>
    <span style="left:680px">Services<i>⌄</i></span>
    <span style="left:780px">Prices<i>⌄</i></span>
    <span style="left:868px">Gallery<i>⌄</i></span>
    <span style="left:966px">About Us</span>
    <span style="left:1072px">Contact Us</span>
  </nav>

  <svg class="play" width="86" height="86" viewBox="0 0 86 86">
    <circle cx="43" cy="43" r="40" fill="none" stroke="rgba(255,255,255,.6)" stroke-width="4"/>
    <path d="M35 27 L61 43 L35 59 Z" fill="rgba(255,255,255,.6)"/>
  </svg>

  <div class="hero-sub">We provide luxury cars on</div>
  <h1 class="hero-title">Rental and Lease</h1>
  <a class="btn-outline-light">REQUEST QUOTE</a>
</header>

<section class="services">
  <h2 class="section-title">Our Services</h2>
  <p class="lead">We are working hard to create a better experience for you. So watch this space, as we unravel the best in travel solutions.</p>

  <div class="service" style="left:127px">
    <svg width="110" height="116" viewBox="0 0 110 116"><path d="M55 3a52 52 0 0 1 9 103.2L55 114l-9-7.8A52 52 0 0 1 55 3z" fill="none" stroke="#c9a04a" stroke-width="1.3"/>
      <rect x="37" y="39" width="36" height="32" rx="2" fill="none" stroke="#c9a04a" stroke-width="2.5"/><line x1="37" y1="47" x2="73" y2="47" stroke="#c9a04a" stroke-width="3"/>
      <g fill="#c9a04a"><rect x="42" y="52" width="5" height="4"/><rect x="50" y="52" width="5" height="4"/><rect x="58" y="52" width="5" height="4"/><rect x="66" y="52" width="4" height="4"/><rect x="42" y="60" width="5" height="4"/><rect x="50" y="60" width="5" height="4"/><rect x="58" y="60" width="5" height="4"/><rect x="66" y="60" width="4" height="4"/></g></svg>
    <h3>Events</h3>
  </div>
  <div class="service" style="left:315px">
    <svg width="110" height="116" viewBox="0 0 110 116"><path d="M55 3a52 52 0 0 1 9 103.2L55 114l-9-7.8A52 52 0 0 1 55 3z" fill="none" stroke="#c9a04a" stroke-width="1.3"/>
      <path d="M72 36c-12 1-22 9-28 22l8 8c13-6 21-16 20-30z" fill="none" stroke="#c9a04a" stroke-width="2.5"/><circle cx="61" cy="48" r="4" fill="#c9a04a"/><path d="M44 58l-7 2 4-8 8-2M52 66l-2 7 8-4 2-8M42 68l-6 6" fill="none" stroke="#c9a04a" stroke-width="2.5"/></svg>
    <h3>Shuttle Services</h3>
  </div>
  <div class="service" style="left:503px">
    <svg width="110" height="116" viewBox="0 0 110 116"><path d="M55 3a52 52 0 0 1 9 103.2L55 114l-9-7.8A52 52 0 0 1 55 3z" fill="none" stroke="#c9a04a" stroke-width="1.3"/>
      <path fill="#c9a04a" d="M70 36c2-2 5-1 4 2l-6 10 5 17-3 3-9-13-7 7 1 6-2 2-4-7-7-4 2-2 6 1 7-7-13-9 3-3 17 5z"/></svg>
    <h3>Airport Limo</h3>
  </div>
  <div class="service" style="left:700px">
    <svg width="110" height="116" viewBox="0 0 110 116"><path d="M55 3a52 52 0 0 1 9 103.2L55 114l-9-7.8A52 52 0 0 1 55 3z" fill="none" stroke="#c9a04a" stroke-width="1.3"/>
      <path fill="#c9a04a" d="M42 44h26l4 9h3v4h-2v12h-6v-4H43v4h-6V57h-2v-4h3zm3 3-3 6h26l-3-6z"/><g fill="#fff"><circle cx="44" cy="59" r="2.5"/><circle cx="66" cy="59" r="2.5"/><rect x="49" y="57" width="12" height="5"/></g></svg>
    <h3>Executive Limo</h3>
  </div>
  <div class="service" style="left:897px">
    <svg width="110" height="116" viewBox="0 0 110 116"><path d="M55 3a52 52 0 0 1 9 103.2L55 114l-9-7.8A52 52 0 0 1 55 3z" fill="none" stroke="#c9a04a" stroke-width="1.3"/>
      <g fill="#c9a04a"><circle cx="55" cy="55" r="7"/><path d="M32 55l9-6v4h4v4h-4v4zM78 55l-9-6v4h-4v4h4v4z"/></g></svg>
    <h3>Point to Point</h3>
  </div>
</section>

<section class="vehicles">
  <h2 class="section-title vehicles-title">Our Vehicles</h2>
  <p class="vehicles-lead">We are working hard to create a better experience for you. So watch this space, as we unravel the best in travel solutions.</p>
  <a class="btn-outline" style="left:910px;top:1117px;width:188px;height:42px">View More Vehicles</a>

  <svg class="arrow" style="left:48px" width="16" height="30" viewBox="0 0 16 30"><path d="M14 2 2 15l12 13" fill="none" stroke="#999" stroke-width="2"/></svg>
  <svg class="arrow" style="left:1128px" width="16" height="30" viewBox="0 0 16 30"><path d="M2 2l12 13L2 28" fill="none" stroke="#999" stroke-width="2"/></svg>

  <div class="vehicle-photo" style="left:99px;background:linear-gradient(180deg,#d9a86a 0%,#a77a52 40%,#4b3b30 70%,#2b2521 100%)" role="img" aria-label="Black off-road SUV parked on a rocky shore at sunset"></div>
  <div class="vehicle-info" style="left:423px">
    <h4>Aster Voyager</h4>
    <ul><li>Manual Transmission</li><li>Seats</li><li>Diesel Fuel type</li></ul>
    <p class="price">Per day <b>$446</b></p>
    <a class="btn-gold">View Details</a>
  </div>

  <div class="vehicle-photo" style="left:636px;background:linear-gradient(180deg,#6f7478 0%,#8a8e90 35%,#5a5e60 65%,#3f4244 100%)" role="img" aria-label="White sedan speeding along a coastal road"></div>
  <div class="vehicle-info" style="left:959px">
    <h4>Aster Voyager</h4>
    <ul><li>Manual Transmission</li><li>Seats</li><li>Diesel Fuel type</li></ul>
    <p class="price">Per day <b>$446</b></p>
    <a class="btn-gold">View Details</a>
  </div>
</section>

<section class="about">
  <div class="about-photo" role="img" aria-label="Blue, white and red sports cars lined up side by side"></div>
  <h2 class="section-title about-title">About Orvane</h2>
  <p class="about-text">Lorem Ipsum is simply dummy text of the printing and type-setting industry. Lorem Ipsum has been the industry's stand-ard dummy text ever since the 1500s, when an unknown printer took a galley of type...</p>
  <a class="btn-outline" style="left:748px;top:1665px;width:132px;height:36px;font-size:10.5px;font-weight:400">Read More Info</a>
</section>

<footer class="footer">
  <div class="testimonial">
    <div class="avatar" role="img" aria-label="Customer portrait"></div>
    <b>Mara Ellison -</b> Lorem Ipsum is simply dummy text of the printing and typesetting industry. Lorem Ipsum has been the industry's standard dummy text ever since the 1500s...
  </div>

  <div class="fcol" style="left:101px">
    <h5>Newsletter Signup</h5>
    <p>Get our recent updates through your email id</p>
    <div class="email-field">Enter your email id</div>
    <a class="fbtn">Subscribe</a>
  </div>
  <div class="fcol" style="left:494px">
    <h5>Welcome</h5>
    <ul><li>Home</li><li>Vehicles</li><li>Services</li><li>Prices</li><li>Gallery</li><li>About us</li></ul>
  </div>
  <div class="fcol" style="left:674px">
    <h5>Information</h5>
    <ul><li>Terms &amp; Conditions</li><li>Privacy policy</li><li>Disclaimer</li><li>Contact us</li><li>Sitemap</li></ul>
  </div>
  <div class="fcol" style="left:907px">
    <h5>Contact Info</h5>
    <p>120 Street name, City name,<br>Country name : 3652235</p>
    <div class="contact-line"><svg width="11" height="11" viewBox="0 0 24 24"><path fill="#c9a04a" d="M6.6 10.8a15 15 0 0 0 6.6 6.6l2.2-2.2c.3-.3.7-.4 1-.2 1.1.4 2.3.6 3.6.6.6 0 1 .4 1 1V20c0 .6-.4 1-1 1A17 17 0 0 1 3 4c0-.6.4-1 1-1h3.5c.6 0 1 .4 1 1 0 1.3.2 2.5.6 3.6.1.3 0 .7-.2 1z"/></svg>( 555 ) 014 2290</div>
    <div class="contact-line"><svg width="12" height="10" viewBox="0 0 24 18"><path fill="#c9a04a" d="M0 0h24v18H0z"/><path d="M1 1l11 8 11-8" fill="none" stroke="#262626" stroke-width="2"/></svg>info@orvane-example.limo</div>
    <div class="tweet"><span></span>1,252</div>
  </div>

  <div class="footer-base">
    <span class="copy">© 2017, orvane. All rights reserved</span>
    <div class="social">Connct with our social network : <span class="dot"></span><span class="dot"></span><span class="dot"></span><span class="dot"></span><span class="dot"></span></div>
  </div>
</footer>

</body>
</html>
```